AUSTRALIAN CONSULTING FIRM BUSINESS CARD - MODERN

We are wanting a modern, clean lined business card design. We are professional niche consultancy firm situated in Australia called Marlow Advisory Partners Pty Ltd.
The card should communicate professionalism and creativity and draw on our logo design (attached).
The design should be two sided, landscape orientation.
Target Market(s)
government, not for profit sector, corporate clients
Industry/Entity Type
Landscape
Requirements
Must have
- logo
no new introduced colours

```html
<!DOCTYPE html>
<html lang="en">
<head>
<meta charset="utf-8">
<title>Marlow Advisory Partners – Business Card</title>
<link href="https://fonts.googleapis.com/css2?family=Didact+Gothic&display=swap" rel="stylesheet">
<style>
  :root {
    --stage: #ecebe8;
    --card-dark: #232323;
    --card-light: #ededed;
    --navy: #1f2f7a;
    --blue: #1a8fd0;
    --royal: #2b3f9e;
    --purple: #8a2f8e;
    --magenta: #b0358f;
    --green: #6cb52d;
    --grey-text: #444;
    --grey-line: #9a9a9a;
    --white-text: #d8d8d8;
  }
  * { box-sizing: border-box; margin: 0; padding: 0; }
  html, body {
    width: 1200px; height: 900px; overflow: hidden;
    background: var(--stage);
    font-family: "Didact Gothic", "Century Gothic", sans-serif;
  }
  .sheet {
    position: relative; width: 1200px; height: 900px;
  }
  .card {
    position: absolute; left: 260px; width: 680px; height: 388px;
    box-shadow: 0 6px 18px rgba(0,0,0,.18);
    overflow: hidden;
  }
  .card--front { top: 42px; background: var(--card-dark); }
  .card--back  { top: 470px; background: var(--card-light); }

  /* front */
  .front-brand {
    position: absolute; left: 70px; top: 118px;
    display: flex; align-items: center; gap: 22px;
  }
  .brand-dot {
    width: 46px; height: 46px; border-radius: 50%;
    background: var(--blue); flex: none;
  }
  .front-brand__name {
    color: var(--royal); font-size: 34px; line-height: 1.15;
    text-transform: uppercase; letter-spacing: 1px;
  }
  .front-web {
    position: absolute; right: 140px; top: 262px;
    color: var(--white-text); font-size: 16px; letter-spacing: 1px;
  }
  .accent-top {
    position: absolute; right: 0; top: 40px; width: 240px; height: 3px;
    background: linear-gradient(90deg, #555 0%, var(--purple) 40%, var(--green) 100%);
  }
  .accent-bottom {
    position: absolute; left: 0; bottom: 34px; width: 250px; height: 3px;
    background: linear-gradient(90deg, var(--blue), var(--royal));
  }

  /* back */
  .back-brand {
    position: absolute; left: 50px; top: 150px; width: 250px;
    display: flex; align-items: center; gap: 16px;
  }
  .back-brand .brand-dot { width: 40px; height: 40px; }
  .back-brand__name {
    color: var(--navy); font-size: 22px; line-height: 1.2;
    text-transform: uppercase;
  }
  .divider {
    position: absolute; left: 320px; top: 120px; width: 2px; height: 150px;
    background: linear-gradient(180deg, transparent, var(--grey-line) 50%, transparent);
  }
  .contact {
    position: absolute; left: 360px; top: 56px; color: var(--grey-text);
    font-size: 15px; line-height: 1.35;
  }
  .contact__name { color: var(--navy); font-size: 24px; text-transform: uppercase; letter-spacing: .5px; }
  .contact__role { font-size: 16px; margin-bottom: 28px; }
  .contact__row { display: flex; gap: 12px; }
  .contact__label { color: var(--navy); font-weight: bold; width: 10px; }
  .contact__email { margin-left: 22px; margin-bottom: 24px; }
  .contact__address { }
  .accent-sweep {
    position: absolute; left: 0; right: 0; bottom: 30px; height: 3px;
    background: linear-gradient(90deg, var(--blue) 0%, var(--royal) 35%, var(--purple) 70%, var(--green) 100%);
  }
</style>
</head>
<body>
<main class="sheet">
  <section class="card card--front" aria-label="Card front">
    <div class="accent-top"></div>
    <div class="front-brand">
      <span class="brand-dot"></span>
      <p class="front-brand__name">Marlow Advisory<br>Partners Pty Ltd</p>
    </div>
    <p class="front-web">www.marlowadvisory.com</p>
    <div class="accent-bottom"></div>
  </section>

  <section class="card card--back" aria-label="Card back">
    <div class="back-brand">
      <span class="brand-dot"></span>
      <p class="back-brand__name">Marlow Advisory Partners</p>
    </div>
    <div class="divider"></div>
    <div class="contact">
      <p class="contact__name">Lena Hartwell</p>
      <p class="contact__role">Operation manager</p>
      <p class="contact__row"><span class="contact__label">T</span><span>+1 555 204 7731</span></p>
      <p class="contact__row"><span class="contact__label">F</span><span>+61 400 555 190</span></p>
      <p class="contact__email">hello@marlowadvisory.com</p>
      <p class="contact__address">Avenue des Palmiers - Bel Air,<br>BP 210 - City, Country</p>
    </div>
    <div class="accent-sweep"></div>
  </section>
</main>
</body>
</html>
```